Magazine Ad Print Design - Premium Italian Winemaking Products

Task Outline:
Create a 1/3 page (4.56 inches wide by 4,88 inches high) square full-color advertisement
Task Description:
Terra Lucente provides home winemakers and vineyards with ultra-premium frozen wine grapes direct from Italy. Terra Lucente grapes are highly unique, as they are the only wine grapes available worldwide that are 100% Organic and have the prestigious Italian DOCG certification. We have developed a patented process for flash-freezing wine grapes, right after being picked off of our wines in Italy. This ensures unparalleled quality for the most discerning winemakers around the world.
In addition to its expanding line of premium wine grapes, Terra Lucente also imports high-quality winemaking equipment, such as wine vats, pumps, buckets, etc.
We are looking for a professional graphic designer to create a print ad for use in a trade magazine. We have recently expanded our offering of grapes from the Chianti region (Sangiovese, Cabernet Sauvignon, Merlot, Trebbiano, and Colorino) to Alba (Barbera, Nebbiolo, Moscato). Additionally, we have recently launched professional-grade winemaking equipment. The Ad should be elegant, clean and modern, yet is approachable to our target consumer (target consumer notes below).
I have attached previous advertisements for an example of the feel that we are looking for. Additionally, a possible idea (file name Idea2.ppt) is attached – it’s very rough and just a possible starting point. The expectation is that the new ad would be more professional/polished.
Other Requirements and Design Guidance
• Reference current website www.terralucente-example.com as a starting point.
• Imagery from current site can be used, and new imagery can be added. Be sure that any new stock photography is authentically Italian (our target consumer will know if this is/is not an Italian vineyard/grape image).
• Feel free to tweak logo slightly, but it must maintain similar look and color scheme.
Brand Objectives
o Educate consumers about the merits of Terra Lucente products
o Stir a passion for our products with well placed imagery and copy
o Compel consumers to learn more about Terra Lucente and act to purchase
o IMPORTANT: Strike the right balance between having an ultra-premium look, yet also providing enough information for consumers. It is important to understand the target consumer (below).
Ad communication priorities.
1. Terra Lucente
2. Premium frozen wine grapes imported from Italy (Sangiovese, Cabernet Sauvignon, Merlot, Trebbiano, Barbera, Nebbiolo, Moscato)
3. Presenting our new line of quality winemaking equipment
4. Contact us or visit website
Overall look should have strong visuals, premium look, clean layout, and informative (yet not too busy).
Target Markets:
1. Intermediate and advanced home winemakers looking for high-quality wine grapes (and equipment) that is authentically Italian. These consumers typically are affluent but earthy. They often read Cellarcraft Journal – the #1 magazine for home winemaking.
2. Small vineyards that are looking to supplement their inventory with high-quality imported wine grapes.
Look and Feel:
• Elegant
• Serious
• Modern/Traditional
• Personable but Professional
• Gender Neutral
• Upmarket

```html
<!DOCTYPE html>
<html lang="en">
<head>
<meta charset="utf-8">
<title>Terra Lucente – Elevating the Art of Wine Making</title>
<link rel="stylesheet" href="https://fonts.googleapis.com/css2?family=Alex+Brush&family=Crimson+Text:ital,wght@0,400;0,700;1,400;1,700&display=swap">
<style>
  :root {
    --wine: #8e1b22;
    --grape: #6a1a22;
    --pour: #d9555a;
    --blush: #f4c4c2;
    --ink: #3a3434;
    --paper: #ffffff;
    --frame: #222222;
  }
  * { margin: 0; padding: 0; box-sizing: border-box; }
  html, body {
    width: 1200px; height: 1000px; overflow: hidden; background: var(--paper);
  }
  .ad {
    position: absolute; left: 143px; top: 13px; width: 915px; height: 973px;
    border: 2px solid var(--frame); background: var(--paper); overflow: hidden;
    font-family: "Crimson Text", Georgia, serif; color: var(--ink);
  }
  .hero-image {
    position: absolute; left: 0; top: 0; width: 340px; height: 971px;
    background: linear-gradient(180deg, var(--grape) 0%, var(--pour) 50%, var(--blush) 100%);
  }
  .headline {
    position: absolute; left: 400px; top: 266px; width: 480px; text-align: center;
    font-family: "Alex Brush", cursive; color: var(--wine);
    font-size: 58px; line-height: 68px; font-weight: 400;
  }
  .features { position: absolute; left: 358px; top: 418px; width: 545px; }
  .feature { margin-bottom: 12px; }
  .feature-label {
    font-style: italic; font-weight: 700; color: var(--wine);
    font-size: 22px; line-height: 28px; letter-spacing: 0.6px;
  }
  .feature-text { font-style: italic; font-size: 22px; line-height: 31px; }
  .credentials {
    margin-top: 10px; font-weight: 700; color: var(--wine);
    font-size: 23px; letter-spacing: 0.3px; display: flex; align-items: center; gap: 10px;
  }
  .credentials .dot {
    width: 7px; height: 7px; background: var(--wine); transform: rotate(45deg); display: inline-block;
  }
  .call-to-action {
    position: absolute; right: 183px; top: 832px; text-align: right;
  }
  .call-to-action p { font-style: italic; font-size: 22px; line-height: 36px; }
  .call-to-action .web-address {
    margin-top: 8px; font-weight: 700; font-style: italic; color: var(--wine); font-size: 23px;
  }
  .brand {
    position: absolute; left: 746px; top: 792px; width: 143px;
    display: flex; flex-direction: column; align-items: center; gap: 10px;
  }
  .brand-square { width: 143px; height: 124px; background: var(--wine); }
  .brand-name {
    font-weight: 700; color: var(--wine); font-size: 15px; letter-spacing: 0.4px; white-space: nowrap;
  }
</style>
</head>
<body>
  <main class="ad">
    <div class="hero-image" role="img"
         aria-label="Photograph of a cluster of red wine grapes with rosé wine splashing down into a wine glass"></div>

    <h1 class="headline">Elevating the art of<br>Wine Making . . .</h1>

    <section class="features">
      <div class="feature">
        <div class="feature-label">WITH OUR . . .</div>
        <div class="feature-text">Patented process for flash-freezing wine grapes,<br>right after being picked off of our wines in Italy</div>
      </div>
      <div class="feature">
        <div class="feature-label">AND OUR . . .</div>
        <div class="feature-text">New line of high-quality wine making equipment</div>
      </div>
      <div class="feature">
        <div class="feature-label">CREATE . . .</div>
        <div class="feature-text">Wines such Sangiovese, Cabernet Sauvignon, Merlot,<br>Trebbiano, Colorino, Barbera, Nebbiolo and Moscato.</div>
      </div>
      <div class="credentials">100% ORGANIC <span class="dot"></span> DOCC CERTIFIED</div>
    </section>

    <section class="call-to-action">
      <p>To learn more about&nbsp; making<br>wines of unparalleled quality, visit…</p>
      <p class="web-address">www.terralucente-example.com</p>
    </section>

    <div class="brand">
      <div class="brand-square"></div>
      <div class="brand-name">TERRA LUCENTE</div>
    </div>
  </main>
</body>
</html>
```